Flyer-Design zum Thema Bewertungsportale DIN lang(9,8 x 21 cm)
Zielgruppe
Zahnklinik mit allen Fachrichtungen
Aufgabenstellung
Modernes und pfiffiges Design, bitte an unserem Corporate-Design orientieren. Generell arbeiten wir in unseren Designs viel mit den Kreisen, welche als Datei beigefügt sind. Die Kreise sind oft in Ecken angeschnitten, mal größer mal kleiner. In dem Fall würde ich 3 verschiedene Farben an Kreisen nehmen, grün muss auf jeden Fall dabei sein. evtl. kann man auch ein schönes Bild bei bildarko.de vorschlagen, was zum Thema Bewertungsportale passt. Zum Beispiel so etwas: https://de.bildarko-beispiel.com/id/118816126 oder https://de.bildarko-beispiel.com/id/110896051 , ich lasse gerade den Text erstellen. Bitte solange Platzhalter verwenden, 4 Absätze, oben eine Begrüßung, Erklärung und dann 3 Absätze mit jeweils einer kurzerklärung zum jeweiligen bewertungsportal. 1. Finvela, 2. kalvira , 3. plauderly am ende ganz unten einen dankessatz. wie gesagt texte kommen noch bitte schonmal Grafiken setzen und schönen Flyer gestalten mit Platzhaltern. auf der Rückseite sollten unsere 3 Labels genannt werden Lumivo°praxis, Lumivo Spange, Lumivo Kinder
vielleicht kann man auch den Einleitungstext auf die Rückseite drauf machen.
Das ist der Text für den Flyer:
Sie sind mit uns zufrieden? Sagen Sie es weiter!
Wir haben Sie fachmännisch behandelt. Wir sind auf Ihre Wünsche und Ängste eingegangen. Atmosphäre und Kommunikation in unserer Praxis stimmen. Sie gehen zufrieden nach Hause und kommen auch das nächste Mal wieder mit einem guten Gefühl zu uns.
Das freut uns sehr. Noch mehr freuen wir uns, wenn Sie uns im Netz bewerten – damit auch online ein richtiges Bild davon entsteht, was wir bei Lumivo°praxis jeden Tag für unsere Patienten leisten.
Deshalb möchten wir Sie hiermit bitten: Machen Sie Ihre gute Meinung über uns öffentlich. Jede positive Rezension bei Finvela, Kalvira oder Plauderly zählt.
So bewerten Sie uns bei Finvela
Geben Sie „Lumivo Praxis' in das Finvela-Suchfeld ein. Links erscheint die Liste der Suchergebnisse, rechts eine Zusam..

```html
<!DOCTYPE html>
<html lang="de">
<head>
<meta charset="utf-8">
<title>Flyer Bewertungsportale – Lumivo Praxis</title>
<link rel="stylesheet" href="https://fonts.googleapis.com/css2?family=Roboto:wght@300;400;500;700&family=Gochi+Hand&display=swap">
<style>
  :root {
    --green: #a9c436;
    --green-pale: #eef2c6;
    --green-faint: #f7f9e6;
    --blue: #8cb8de;
    --text: #454545;
    --label: #3a3a3a;
    --band-grey: #f1f1f1;
    --photo-grey: #c9c9c9;
    --white: #ffffff;
  }
  * { margin: 0; padding: 0; box-sizing: border-box; }
  html, body { width: 1112px; height: 1200px; overflow: hidden; background: var(--white); }
  body { font-family: "Roboto", Arial, sans-serif; color: var(--text); }
  .flyer { position: relative; width: 1112px; height: 1200px; overflow: hidden; background: var(--white); }
  .decor { position: absolute; inset: 0; }
  .abs { position: absolute; }

  .divider { position: absolute; left: 556px; top: 0; width: 3px; height: 1200px; background: #111; }

  /* left column */
  .headline-band {
    left: 0; top: 104px; width: 470px; height: 48px;
    background: var(--green-pale); border-radius: 0 24px 24px 0;
    display: flex; align-items: center; padding-left: 26px;
    font-weight: 700; font-size: 23px; letter-spacing: 2.4px; color: var(--green);
  }
  .headline-band span { font-weight: 400; margin-left: 8px; }
  .tagline-pill {
    left: 248px; top: 163px; width: 310px; height: 50px;
    background: var(--green-pale); border-radius: 25px 0 0 25px;
    display: flex; align-items: center; padding-left: 20px;
    font-family: "Gochi Hand", cursive; font-size: 28px; color: var(--blue); letter-spacing: 1px;
  }
  .tagline-pill i {
    display: inline-block; width: 12px; height: 12px; border: 2.5px solid var(--green);
    border-radius: 50%; margin-right: 18px;
  }
  .intro { left: 36px; width: 506px; font-weight: 300; font-size: 17.6px; line-height: 24.5px; letter-spacing: 0.35px; }
  .intro.justify { text-align: justify; hyphens: manual; }
  .intro .highlight { color: var(--green); font-weight: 400; display: block; padding-left: 48px; }

  .photo-band {
    left: 0; top: 589px; width: 557px; height: 259px; background: var(--photo-grey);
    border-top: 3px solid var(--blue); border-bottom: 3px solid var(--blue);
  }
  .photo-slot {
    left: 72px; top: 603px; width: 428px; height: 229px; border-radius: 14px;
    background: radial-gradient(ellipse at 50% 40%, #ffffff 0%, #eceff1 55%, #d6dadd 100%);
  }

  .label { left: 0; width: 557px; text-align: center; color: var(--label); }
  .label-name { font-weight: 300; letter-spacing: -0.3px; }
  .label-sub { font-size: 8.6px; font-weight: 400; color: #333; margin-top: 2px; }
  .dash { left: 214px; width: 137px; border-top: 1.5px dashed #d5d5d5; }

  /* right column */
  .portal-band {
    left: 560px; width: 552px; height: 44px; background: var(--band-grey);
    border-top: 2px solid var(--green); border-bottom: 2px solid var(--green);
    display: flex; align-items: center; padding-left: 53px;
    font-weight: 500; font-size: 18px; color: #333;
  }
  .portal-band b { font-weight: 500; color: var(--blue); margin-left: 5px; }
  .portal-badge {
    position: absolute; right: 23px; top: -3px; width: 46px; height: 46px;
    border: 2.5px solid var(--green); border-radius: 50%; background: var(--white);
  }
  .steps { left: 600px; width: 480px; list-style: none; font-weight: 300; font-size: 15.8px; line-height: 24.3px; }
  .steps li { position: relative; padding-left: 13px; margin-bottom: 6px; }
  .steps li::before {
    content: ""; position: absolute; left: -1px; top: 7px; width: 10px; height: 10px;
    border: 2px solid var(--blue); border-radius: 50%; box-sizing: border-box;
  }
  .steps .note { font-size: 13px; }
  .thanks { left: 560px; top: 843px; width: 552px; text-align: center; font-weight: 500; font-size: 18px; line-height: 22px; color: #333; }
  .signoff {
    left: 596px; top: 958px; width: 516px; height: 108px; background: var(--green-pale);
    border-radius: 22px 0 0 22px; display: flex; align-items: center; justify-content: flex-end;
    padding-right: 28px; font-family: "Gochi Hand", cursive; font-size: 31px; color: var(--green); letter-spacing: 1px;
  }
</style>
</head>
<body>
<main class="flyer">
  <svg class="decor" width="1112" height="1200" viewBox="0 0 1112 1200" aria-hidden="true">
    <circle cx="80" cy="-30" r="275" fill="var(--green-faint)"/>
    <circle cx="15" cy="-20" r="55" fill="none" stroke="var(--green-pale)" stroke-width="18"/>
    <circle cx="590" cy="1300" r="320" fill="var(--green-faint)"/>
    <circle cx="820" cy="1380" r="400" fill="var(--green-faint)"/>
    <circle cx="570" cy="1210" r="82" fill="none" stroke="var(--green-pale)" stroke-width="26"/>
  </svg>

  <div class="divider"></div>

  <h1 class="abs headline-band">SIE SIND MIT UNS ZUFRIEDEN?<span>-</span></h1>
  <p class="abs tagline-pill"><i></i>Sagen Sie es weiter!</p>

  <p class="abs intro justify" style="top:251px">Wir haben Sie fachmännisch behandelt. Wir sind auf Ihre Wün&shy;sche und Ängste eingegangen. Atmosphäre und Kommuni&shy;kation in unserer Praxis stimmen. Sie gehen zufrieden nach Hause und kommen auch das nächste Mal wieder mit einem guten Gefühl zu uns. Das freut uns sehr.</p>
  <p class="abs intro justify" style="top:397px">Noch mehr freuen wir uns, wenn Sie uns im Netz bewerten - damit auch online ein richtiges Bild davon entsteht, was wir bei Lumivo°praxis jeden Tag für unsere Patienten leisten.</p>
  <p class="abs intro" style="top:487px">Deshalb möchten wir Sie hiermit bitten:<span class="highlight">Machen Sie Ihre gute Meinung über uns öffentlich.</span>Jede positive Rezension bei Finvela, Kalvira oder Plauderly zählt.</p>

  <div class="abs photo-band"></div>
  <div class="abs photo-slot" role="img" aria-label="Bild: Hand tippt auf fünf leuchtende Bewertungssterne vor hellem Hintergrund"></div>

  <div class="abs label" style="top:888px">
    <div class="label-name" style="font-size:27px">Lumivo Spange</div>
    <div class="label-sub">Kieferorthopädie für Kinder, Jugendliche und Erwachsene</div>
  </div>
  <div class="abs dash" style="top:965px"></div>
  <div class="abs label" style="top:994px">
    <div class="label-name" style="font-size:37px">Lumivo Praxis</div>
    <div class="label-sub" style="font-size:10.5px">Zahnmedizin für alle</div>
  </div>
  <div class="abs dash" style="top:1082px"></div>
  <div class="abs label" style="top:1110px">
    <div class="label-name" style="font-size:27px">Lumivo Kinder</div>
    <div class="label-sub" style="font-size:8px">Zahnärztl. Gemeinschaftspraxis für Kinder &amp; Jugendliche</div>
  </div>

  <h2 class="abs portal-band" style="top:62px">So bewerten Sie uns bei<b>Finvela</b><span class="portal-badge"></span></h2>
  <ul class="abs steps" style="top:118px">
    <li>Geben Sie „Lumivo Praxis“ in das Finvela-Suchfeld ein.</li>
    <li>Links erscheint die Liste der Suchergebnisse, rechts eine Zusammenfassung von Informationen zu unserer Praxis.</li>
    <li>Klicken sie auf den neben den Bewertungssternen erscheinenden Linktext „Finvela-Rezensionen“, dann auf „Rezension schreiben“.</li>
    <li>Jetzt können Sie Ihre Sternchen hinterlassen.<br>Schön wäre es auch, wenn Sie noch einen kleinen Text schreiben.</li>
  </ul>

  <h2 class="abs portal-band" style="top:344px">So bewerten Sie uns bei<b>Kalvira</b><span class="portal-badge"></span></h2>
  <ul class="abs steps" style="top:399px">
    <li>Auf Deutschlands größtem Arztempfehlungsportal<br>kalvira.de finden Sie uns, indem Sie „mvz lumivo praxis“<br>ins Suchfenster eingeben.</li>
    <li>Bei unserem Profil angelangt, klicken Sie auf „Zahnärzte bewerten“.</li>
    <li>Jetzt suchen Sie in der Liste Ihren Behandler und hinterlassen<br>Ihr detailliertes Feedback.</li>
  </ul>

  <h2 class="abs portal-band" style="top:604px">So bewerten Sie uns bei<b>Plauderly</b><span class="portal-badge"></span></h2>
  <ul class="abs steps" style="top:660px">
    <li>Suchen Sie bei www.plauderly.de nach lumivo praxis.<br>Jetzt können Sie sofort loslegen:</li>
    <li>Einfach bei „Bewertungen“ Sternchen markieren und<br>Bewertungstext eingeben.<br><span class="note">(Das funktioniert nur, wenn Sie Plauderly-Mitglied und eingeloggt sind.)</span></li>
  </ul>

  <p class="abs thanks">Ganz herzlichen Dank für Ihre Bewertung(en) –<br>und bis zum nächsten Termin! Wir freuen uns auf Sie!</p>
  <p class="abs signoff">Ihr Lumivo°praxis Team Düsseldorf</p>
</main>
</body>
</html>
```